Rig up a website for a Rigging Company

We already have a logo. Looking for a website design that works on plinvara.com.
Our rigging company uses semi trucks, forklifts, and similar equipment to move large machines.
Our logo is white, black and red.

Target Market(s)

Medical Industry (moving medical equipment), Utility Industry (power equipment), Food Industry (moving bottling/packing equipment), US Government (large equipment)

Industry/Entity Type

It Company

Coding

Coded - Design and coding required

Number of Pages Required

5+ page

Font styles to use
Sans Serif

Colors
ec1f27
ffffff
0355a3

Requirements
Must have
• Home page, About page, Services Page, and Contact Information page
Nice to have
• Pictures of semi and forklifts and ability to insert our own pictures of our equipment

```html
<!DOCTYPE html>
<html lang="en">
<head>
<meta charset="utf-8">
<title>Kestrel Rigging</title>
<link href="https://fonts.googleapis.com/css2?family=Montserrat:wght@400;500;600;700&family=Open+Sans:wght@400;600&display=swap" rel="stylesheet">
<style>
:root{
  --red:#e81e25;
  --dark:#262324;
  --darker:#1d1b1c;
  --ink:#1e1e1e;
  --muted:#8a8a8a;
  --light:#f1f1f1;
  --card:#eeeeee;
  --white:#ffffff;
  --orange:#cf5a2b;
  --slate:#4b5b82;
  --sky:#3e9fc9;
  --green:#3ea24c;
}
*{margin:0;padding:0;box-sizing:border-box}
html,body{width:1200px;height:3371px;overflow:hidden}
body{position:relative;background:var(--white);font-family:"Open Sans",Arial,sans-serif;color:var(--ink)}
.abs{position:absolute}
.heading{font-family:"Montserrat",Arial,sans-serif;font-weight:600;font-size:21px;text-align:center;width:100%;left:0}
.subline{font-size:12px;color:var(--muted);text-align:center;width:100%;left:0}
.rule{width:36px;height:3px;background:var(--red);left:582px}
/* header */
.brand{left:209px;top:10px;font-family:"Montserrat",sans-serif;font-weight:700;font-size:25px;color:var(--ink);letter-spacing:-.5px}
.brand-mark{display:inline-block;width:12px;height:12px;background:var(--red);margin-right:7px;vertical-align:2px}
.contact-mail{left:732px;top:23px;font-size:11px;color:#444;display:flex;align-items:center;gap:6px}
.contact-phone{left:862px;top:17px;font-family:"Montserrat",sans-serif;font-size:18px;color:#333;display:flex;align-items:center;gap:7px}
.nav{left:0;top:63px;width:1200px;height:29px;background:var(--darker)}
.nav a{position:absolute;top:0;height:29px;line-height:29px;font-family:"Montserrat",sans-serif;font-size:11.5px;color:#ddd;text-decoration:none}
.nav .active{background:var(--red);color:#fff;padding:0 22px;left:213px;clip-path:polygon(6% 0,100% 0,94% 100%,0 100%)}
.nav-social{position:absolute;top:9px;display:flex;gap:12px;left:921px}
.nav-social span{width:10px;height:10px;background:#ddd;border-radius:2px}
.nav-social span:first-child{background:var(--red)}
/* hero */
.hero{left:0;top:92px;width:1200px;height:391px;background:linear-gradient(180deg,#5d6664 0%,#7b8180 45%,#6e6a58 70%,#3d4034 100%)}
.hero-band{left:490px;top:366px;width:710px;height:117px;background:var(--red);clip-path:polygon(14% 0,100% 0,100% 100%,0 100%)}
.hero-title{left:600px;top:393px;font-family:"Montserrat",sans-serif;font-weight:500;font-size:24px;line-height:34px;color:#fff}
.arrow{top:272px}
/* why */
.why-card{top:613px;width:180px;height:178px;background:var(--card);text-align:center}
.why-card.featured{background:var(--red);color:#fff}
.why-icon{position:absolute;left:60px;top:27px;width:60px;height:60px;border-radius:50%;background:#333;display:flex;align-items:center;justify-content:center}
.featured .why-icon{background:transparent;border:2px solid #fff}
.why-text{position:absolute;left:18px;right:18px;top:106px;font-size:11px;line-height:15px}
.why-tag{position:absolute;left:76px;bottom:-4px;width:28px;height:14px;background:#333;clip-path:polygon(20% 0,100% 0,80% 100%,0 100%)}
.featured .why-tag{background:#fff}
/* services */
.services{left:0;top:845px;width:1200px;height:530px;background:var(--dark)}
.service{top:989px;width:300px;height:386px}
.service-photo{position:absolute;left:0;top:0;width:100%;height:292px}
.service-label{position:absolute;left:0;bottom:0;width:100%;height:94px;line-height:94px;text-align:center;font-family:"Montserrat",sans-serif;font-weight:500;font-size:17px;color:#fff}
.service.raised{top:973px;height:418px;box-shadow:0 6px 18px rgba(0,0,0,.35)}
.service.raised .service-photo{height:308px}
.service.raised .service-label{height:110px;line-height:110px}
/* work */
.tile{background:#999}
.tile.feature{background:var(--red);color:#fff;font-family:"Montserrat",sans-serif;font-size:14px;font-weight:500;display:flex;flex-direction:column;align-items:center;justify-content:center;gap:10px}
/* news */
.news{left:0;top:1991px;width:1200px;height:739px;background:var(--light)}
.news-photo{background:#555}
.news-body{width:250px}
.news-title{font-family:"Montserrat",sans-serif;font-weight:600;font-size:12.5px;line-height:17px}
.news-meta{margin-top:12px;border-left:2px solid var(--red);padding-left:12px;font-size:10.5px;color:#666}
.news-meta b{color:var(--red);font-weight:400;margin-right:8px}
.news-meta p{margin-top:9px;line-height:16px}
.read-more{display:block;margin-top:14px;font-size:11px;color:var(--red);font-weight:600}
.btn{background:var(--red);color:#fff;font-family:"Montserrat",sans-serif;font-size:11px;text-align:center;clip-path:polygon(8% 0,100% 0,92% 100%,0 100%)}
/* newsletter */
.news-input{left:348px;top:2852px;width:362px;height:30px;border-bottom:1px solid #ccc;font-size:11px;color:#555;padding-left:2px;line-height:30px}
/* footer */
.footer{left:0;top:2953px;width:1200px;height:418px;background:var(--dark);color:#fff}
.foot-col{top:3067px;width:270px;text-align:center;color:#ccc}
.foot-divider{top:3062px;width:1px;height:130px;background:#444}
.foot-social{left:526px;top:3240px;display:flex;gap:2px}
.foot-social span{width:50px;height:40px;background:#555;clip-path:polygon(25% 0,100% 0,75% 100%,0 100%);display:flex;align-items:center;justify-content:center}
.foot-social span:first-child{background:var(--red)}
.foot-social i{width:9px;height:9px;background:#fff;border-radius:50%}
.copyright{top:3315px;left:0;width:100%;text-align:center;font-size:11px;color:#aaa}
</style>
</head>
<body>

<!-- header -->
<div class="abs brand"><span class="brand-mark"></span>Kestrel Rigging</div>
<div class="abs contact-mail">
  <svg width="12" height="9" viewBox="0 0 12 9"><rect width="12" height="9" rx="1" fill="#e81e25"/><path d="M0 1 6 5 12 1" stroke="#fff" fill="none"/></svg>
  info@plinvara.com
</div>
<div class="abs contact-phone">
  <svg width="14" height="18" viewBox="0 0 14 18"><rect x="1" y="0" width="12" height="18" rx="2" fill="#e81e25"/><rect x="3" y="2" width="8" height="11" fill="#fff"/></svg>
  (555) 014 2290
</div>
<nav class="abs nav">
  <a class="active" href="#">Home</a>
  <a href="#" style="left:318px">About Us</a>
  <a href="#" style="left:418px">Services</a>
  <a href="#" style="left:505px">Work</a>
  <a href="#" style="left:578px">Equipment</a>
  <a href="#" style="left:690px">News</a>
  <a href="#" style="left:768px">Contact Us</a>
  <div class="nav-social"><span></span><span></span><span></span></div>
</nav>

<!-- hero -->
<div class="abs hero" role="img" aria-label="Heavy industrial load on a low-loader trailer under a cloudy sky"></div>
<svg class="abs arrow" style="left:118px" width="30" height="24" viewBox="0 0 30 24"><path d="M28 12H3M12 3 3 12l9 9" stroke="#fff" stroke-width="2.5" fill="none"/></svg>
<svg class="abs arrow" style="left:1052px" width="30" height="24" viewBox="0 0 30 24"><path d="M2 12h25M18 3l9 9-9 9" stroke="#fff" stroke-width="2.5" fill="none"/></svg>
<div class="abs hero-band"></div>
<div class="abs hero-title">Kestrel Rigging Knows<br>How to move your Equipment</div>

<!-- why choose us -->
<h2 class="abs heading" style="top:521px">Why Choose Us</h2>
<p class="abs subline" style="top:549px">Lorem ipsum dolor sit amet, consectetur adipiscing elit.</p>
<div class="abs rule" style="top:574px"></div>

<div class="abs why-card" style="left:209px">
  <div class="why-icon"><svg width="28" height="30" viewBox="0 0 28 30"><circle cx="14" cy="11" r="9" fill="#fff"/><circle cx="14" cy="11" r="4" fill="#333"/><path d="M8 18 5 29l5-3 3 3 1-9M20 18l3 11-5-3-3 3-1-9" fill="#fff"/></svg></div>
  <p class="why-text">17 years of business excellence</p>
  <span class="why-tag"></span>
</div>
<div class="abs why-card featured" style="left:409px">
  <div class="why-icon"><svg width="34" height="22" viewBox="0 0 34 22"><rect x="1" y="4" width="20" height="11" fill="#fff"/><path d="M21 7h7l5 5v3H21z" fill="#fff"/><circle cx="8" cy="18" r="3" fill="#fff"/><circle cx="26" cy="18" r="3" fill="#fff"/></svg></div>
  <p class="why-text">Dedicated to the supply of quality products</p>
  <span class="why-tag"></span>
</div>
<div class="abs why-card" style="left:611px">
  <div class="why-icon"><svg width="28" height="28" viewBox="0 0 28 28"><circle cx="14" cy="14" r="9" fill="#fff"/><g stroke="#fff" stroke-width="4"><path d="M14 1v26M1 14h26M5 5l18 18M23 5 5 23"/></g><circle cx="14" cy="14" r="4" fill="#333"/></svg></div>
  <p class="why-text">Committed to providing the best services</p>
  <span class="why-tag"></span>
</div>
<div class="abs why-card" style="left:811px">
  <div class="why-icon"><svg width="30" height="26" viewBox="0 0 30 26"><path d="M5 12 8 4h14l3 8" stroke="#fff" stroke-width="2.5" fill="none"/><rect x="2" y="12" width="26" height="8" rx="2" fill="#fff"/><rect x="4" y="20" width="5" height="4" fill="#fff"/><rect x="21" y="20" width="5" height="4" fill="#fff"/></svg></div>
  <p class="why-text">Never compromising safety</p>
  <span class="why-tag"></span>
</div>

<!-- services -->
<section class="abs services"></section>
<h2 class="abs heading" style="top:880px;color:#fff">Our Services</h2>
<p class="abs subline" style="top:908px;color:#aaa">Lorem ipsum dolor sit amet, consectetur adipiscing elit.</p>
<div class="abs rule" style="top:933px"></div>

<div class="abs service" style="left:0">
  <div class="service-photo" role="img" aria-label="Yellow heavy loader machine ready for specialty rigging" style="background:linear-gradient(160deg,#6d6a4e,#3b3a2c)"></div>
  <div class="service-label" style="background:var(--orange)">Specialty Rigging</div>
</div>
<div class="abs service" style="left:600px">
  <div class="service-photo" role="img" aria-label="Yellow excavator and crane on a building site" style="background:linear-gradient(160deg,#8fa3b7,#8e7a52)"></div>
  <div class="service-label" style="background:var(--sky)">Crane Services</div>
</div>
<div class="abs service" style="left:900px">
  <div class="service-photo" role="img" aria-label="Warehouse interior with racking and stored equipment" style="background:linear-gradient(160deg,#6c7582,#3f4650)"></div>
  <div class="service-label" style="background:var(--green)">Storage and Warehousing</div>
</div>
<div class="abs service raised" style="left:299px">
  <div class="service-photo" role="img" aria-label="White semi truck cab raised on a maintenance lift" style="background:linear-gradient(170deg,#d9dadb,#9e9fa2 70%,#a33 100%)"></div>
  <div class="service-label" style="background:var(--slate)">Maintenance</div>
</div>

<!-- recent work -->
<h2 class="abs heading" style="top:1426px">Recent Work</h2>
<p class="abs subline" style="top:1455px">Lorem ipsum dolor sit amet, consectetur adipiscing elit.</p>
<div class="abs rule" style="top:1480px"></div>

<div class="abs tile" role="img" aria-label="Red crushing plant loaded on a flatbed trailer" style="left:209px;top:1521px;width:389px;height:209px;background:linear-gradient(170deg,#c9d6de,#9a4a3a 65%,#6d6a60)"></div>
<div class="abs tile feature" style="left:604px;top:1521px;width:187px;height:209px">
  <svg width="16" height="16" viewBox="0 0 16 16"><path d="M2 14 14 2M9 2h5v5M7 14H2V9" stroke="#fff" stroke-width="2" fill="none"/></svg>
  Lorem ipsum
</div>
<div class="abs tile" role="img" aria-label="Workers beside a tall industrial tower with a flag" style="left:800px;top:1521px;width:191px;height:209px;background:linear-gradient(170deg,#c6ccd2,#8a8880)"></div>
<div class="abs tile" role="img" aria-label="Crew moving a large electrical cabinet" style="left:209px;top:1737px;width:191px;height:209px;background:linear-gradient(170deg,#a9abae,#5e6266)"></div>
<div class="abs tile" role="img" aria-label="Crane lifting a heavy drum under blue sky" style="left:407px;top:1737px;width:191px;height:209px;background:linear-gradient(170deg,#7fa6d3,#6f7370)"></div>
<div class="abs tile" role="img" aria-label="Large white yacht being transported over water" style="left:604px;top:1737px;width:387px;height:209px;background:linear-gradient(180deg,#b7c4cc,#d9d9d6 55%,#4d5b5d)"></div>

<!-- news -->
<section class="abs news"></section>
<h2 class="abs heading" style="top:2026px">News &amp; Events</h2>
<p class="abs subline" style="top:2055px">Lorem ipsum dolor sit amet, consectetur adipiscing elit.</p>
<div class="abs rule" style="top:2080px"></div>

<div class="abs news-photo" role="img" aria-label="Two business partners shaking hands in a workshop" style="left:276px;top:2121px;width:380px;height:236px;background:linear-gradient(160deg,#8a7a3a,#3a3634)"></div>
<article class="abs news-body" style="left:683px;top:2137px">
  <h3 class="news-title">Praesent euismod ante sed faucibus vehicula.</h3>
  <div class="news-meta"><b>Relocate Equipment</b>23 / 2/ 2017
    <p>Lorem ipsum dolor sit amet, consectetur adipiscing elit. Sed viverra consequat odio, ut placerat libero tempor ut. Praesent euismod ante sed faucibus vehicula.......</p>
  </div>
  <a class="read-more">Read More &raquo;</a>
</article>

<article class="abs news-body" style="left:274px;top:2395px">
  <h3 class="news-title">Praesent euismod ante sed faucibus vehicula.</h3>
  <div class="news-meta"><b>Relocate Equipment</b>23 / 2/ 2017
    <p>Lorem ipsum dolor sit amet, consectetur adipiscing elit. Sed viverra consequat odio, ut placerat libero tempor ut. Praesent euismod ante sed faucibus vehicula.......</p>
  </div>
  <a class="read-more">Read More &raquo;</a>
</article>
<div class="abs news-photo" role="img" aria-label="Mobile crane lifting a generator onto a truck" style="left:544px;top:2389px;width:380px;height:236px;background:linear-gradient(180deg,#6d9ed6,#c9d3dc 45%,#4e6a3a)"></div>

<div class="abs btn" style="left:539px;top:2663px;width:122px;height:27px;line-height:27px">View More &raquo;</div>

<!-- newsletter -->
<h2 class="abs heading" style="top:2768px">Newsletter</h2>
<p class="abs subline" style="top:2797px">Lorem ipsum dolor sit amet, consectetur adipiscing elit.</p>
<div class="abs rule" style="top:2822px"></div>
<div class="abs news-input">Enter Your Email</div>
<div class="abs btn" style="left:703px;top:2883px;width:126px;height:27px;line-height:27px">Subscribe</div>

<!-- footer -->
<footer class="abs footer"></footer>
<h2 class="abs heading" style="top:2988px;color:#fff">Get In Touch</h2>
<p class="abs subline" style="top:3017px;color:#aaa">Lorem ipsum dolor sit amet, consectetur adipiscing elit.</p>
<div class="abs rule" style="top:3042px"></div>

<div class="abs foot-col" style="left:195px">
  <svg width="34" height="34" viewBox="0 0 34 34"><path d="M8 3 13 9 10 13c2 5 6 9 11 11l4-3 6 5-4 5C16 31 3 18 3 7z" stroke="#ccc" stroke-width="1.6" fill="none"/></svg>
  <p style="margin-top:30px;font-family:Montserrat,sans-serif;font-size:15px">Call: (555) 014 2290</p>
</div>
<div class="abs foot-divider" style="left:465px"></div>
<div class="abs foot-col" style="left:465px">
  <svg width="26" height="34" viewBox="0 0 26 34"><path d="M13 32C5 20 2 15 2 11a11 11 0 0 1 22 0c0 4-3 9-11 21z" stroke="#ccc" stroke-width="1.6" fill="none"/><circle cx="13" cy="11" r="4" stroke="#ccc" stroke-width="1.6" fill="none"/></svg>
  <p style="margin-top:8px;font-size:12px;color:#fff">Kestrel Rigging</p>
  <p style="font-size:11px;line-height:16px">118 Harbour Lane, Unit 4,<br>Marlow, ON K2P 3R7</p>
</div>
<div class="abs foot-divider" style="left:735px"></div>
<div class="abs foot-col" style="left:735px">
  <svg width="44" height="30" viewBox="0 0 44 30"><rect x="1" y="1" width="42" height="28" stroke="#ccc" stroke-width="1.6" fill="none"/><path d="M1 1 22 17 43 1M1 29l15-15M43 29 28 14" stroke="#ccc" stroke-width="1.6" fill="none"/></svg>
  <p style="margin-top:10px;font-size:12px">E-mail Us</p>
  <p style="font-size:11px;color:var(--red)">office@plinvara.com</p>
</div>

<div class="abs foot-social"><span><i></i></span><span><i></i></span><span><i></i></span></div>
<p class="abs copyright">© Copyright 2017 Kestrel Rigging. All Rights Reserved</p>

</body>
</html>
```